Fish Farm needing 3 - Fold Flyer / Price List designed

We are looking for a new Price List for our Fish Farm. I have attached an example of the basic info that needs in the flyer. We want the flyer to be a 3 fold page. Anything that is on our website, you can use for ideas. There are some pictures on there that can be photoshopped into the flyer. Do not use any photos from any other sites. We are looking for something professional but fun and exciting! I have also attached our business logo. We tend to stay with the blues and greens for colors. Let's get started....
Updates

Need extra days to review

Contact Information for Business Card

We are needing a business card with our new logo on it. We also need our address, phone numbers, email address, and website listed. Please view our website for more ideas.

Colors

Designer to choose colors to be used in the design.

```html
<!DOCTYPE html>
<html lang="en">
<head>
<meta charset="utf-8">
<title>Brookline Fish Farm – Price List</title>
<link href="https://fonts.googleapis.com/css2?family=Sniglet:wght@800&family=Open+Sans:wght@400;600;700&display=swap" rel="stylesheet">
<style>
  :root{
    --navy:#2b3a9e;
    --blue:#1b75c4;
    --ink:#222;
    --panel-light:#ffffff;
    --panel-shade:#e6e6e6;
    --mid-top:#1a78c6;
    --mid-bottom:#2a4fa6;
    --rule:#c7c7c7;
    --rule-dark:#17559c;
    --white:#fff;
  }
  *{margin:0;padding:0;box-sizing:border-box}
  html,body{width:1200px;height:1015px;overflow:hidden;background:#fff}
  body{font-family:"Open Sans",sans-serif;font-weight:600;color:var(--ink)}
  .flyer{position:relative;width:1200px;height:1015px}
  .panel{position:absolute;top:0;width:400px;height:1015px;overflow:hidden}
  .panel--left{left:0;background:linear-gradient(180deg,var(--panel-light) 20%,var(--panel-shade))}
  .panel--mid{left:400px;background:linear-gradient(180deg,var(--mid-top),var(--mid-bottom));color:var(--white)}
  .panel--right{left:800px;background:linear-gradient(180deg,var(--panel-light) 20%,var(--panel-shade))}
  .photo{position:absolute;left:0;width:400px}
  .photo--top{top:0;height:250px}
  .photo--bottom{top:700px;height:315px}
  .heading{position:absolute;left:0;width:400px;text-align:center;font-family:"Sniglet",cursive;font-weight:800;font-size:29px;line-height:32px;color:var(--navy);letter-spacing:.5px}
  .sub{position:absolute;left:0;width:400px;text-align:center;font-weight:400;font-size:21px;line-height:26px}
  .panel--left .sub,.panel--right .sub.sub--blue{color:var(--blue)}
  .panel--right .sub{color:#333}
  .rule{position:absolute;left:32px;width:336px;height:1px;background:var(--rule)}
  .panel--mid .rule{left:36px;width:328px;background:var(--rule-dark);height:2px}
  .table{position:absolute;display:grid;font-size:15px;line-height:21px}
  .table .th{color:var(--blue);font-weight:700}
  .panel--mid .table .th{color:var(--white)}
  .lines{position:absolute;left:0;width:400px;text-align:center;font-size:15px;line-height:21px}
  .note{position:absolute;left:0;width:400px;text-align:center;font-weight:700;font-size:20px;line-height:25px;color:var(--navy)}
  .note--blue{color:var(--blue)}
  .dots{position:absolute;left:52px;width:296px;border-top:1px dotted #888}
  .brand{position:absolute;left:0;width:400px;top:952px;display:flex;justify-content:center;align-items:center;gap:8px;font-weight:700;font-size:24px;color:var(--navy)}
  .brand-dot{width:14px;height:14px;border-radius:50%;background:var(--blue)}
</style>
</head>
<body>
<div class="flyer">

  <!-- Left panel -->
  <section class="panel panel--left">
    <svg class="photo photo--top" viewBox="0 0 400 250" role="img" aria-label="Photo of a hand holding a bluegill sunfish">
      <defs><linearGradient id="gl" x1="0" y1="0" x2="1" y2="1"><stop offset="0" stop-color="#6a7a52"/><stop offset=".5" stop-color="#b99a7e"/><stop offset="1" stop-color="#3e4a34"/></linearGradient></defs>
      <path d="M0 0H400V150Q200 314 0 150Z" fill="url(#gl)"/>
      <path d="M0 150Q200 314 400 150" fill="none" stroke="#2b3a9e" stroke-width="9"/>
      <path d="M0 160Q200 324 400 160" fill="none" stroke="#4a5fc0" stroke-width="2" stroke-dasharray="6 5"/>
    </svg>

    <h2 class="heading" style="top:276px">hybrid bluegill</h2>
    <p class="sub" style="top:310px">(HYBRID SUNFISH)</p>
    <div class="table" style="top:342px;left:42px;grid-template-columns:108px 84px 88px auto">
      <span class="th">Size</span><span class="th">Each</span><span class="th">1000</span><span class="th">3000</span>
      <span>1-3 Inch</span><span>50¢</span><span>45¢</span><span>40¢</span>
      <span>3-5 Inch</span><span>80¢</span><span>75¢</span><span></span>
      <span>*5-7 Inch</span><span>$1.75</span><span></span><span></span>
    </div>
    <div class="rule" style="top:437px"></div>

    <h2 class="heading" style="top:446px">regular bluegill</h2>
    <div class="table" style="top:482px;left:83px;grid-template-columns:109px 84px auto">
      <span class="th">Size</span><span class="th">Each</span><span class="th">1000</span>
      <span>1-3 Inch</span><span>50¢</span><span>45¢</span>
      <span>*3-5 Inch</span><span>80¢</span><span>75¢</span>
    </div>
    <div class="rule" style="top:552px"></div>

    <h2 class="heading" style="top:563px">redear sunfish</h2>
    <div class="table" style="top:603px;left:83px;grid-template-columns:109px 84px auto">
      <span class="th">Size</span><span class="th">Each</span><span class="th">1000</span>
      <span>1-3 Inch</span><span>50¢</span><span>45¢</span>
      <span>*3-4 Inch</span><span>75¢</span><span>70¢</span>
      <span>*4-5 Inch</span><span>$1.00</span><span>95¢</span>
    </div>
    <div class="rule" style="top:696px"></div>

    <h2 class="heading" style="top:709px">largemouth bass</h2>
    <div class="table" style="top:749px;left:112px;grid-template-columns:136px auto">
      <span class="th">Size</span><span class="th">Each</span>
      <span>3 Inch</span><span>$1.10</span>
      <span>3-4 Inch</span><span>$1.20</span>
      <span>*4-6 Inch</span><span>$1.95</span>
      <span>*6-8 Inch</span><span>$2.75</span>
    </div>
    <div class="rule" style="top:862px"></div>

    <p class="note" style="top:873px">*When Available. Sizes Vary<br>Depending on Time of Year</p>

    <div class="brand"><span class="brand-dot"></span><span>Brookline Fish Farm</span></div>
  </section>

  <!-- Middle panel -->
  <section class="panel panel--mid">
    <h2 class="heading" style="top:35px">triploid grass carp</h2>
    <p class="sub" style="top:69px">(INDIANA PRICES)</p>
    <div class="table" style="top:103px;left:54px;grid-template-columns:176px auto;line-height:25.3px">
      <span>8-11 Inch</span><span>Minimum 5</span>
      <span>5-24 Grass Carp</span><span>$16.00 each</span>
      <span>25-49 Grass Carp</span><span>$15.00 each</span>
      <span>50-99 Grass Carp</span><span>$14.00 each</span>
      <span>100+ Grass Carp</span><span>Inquire</span>
    </div>
    <div class="rule" style="top:242px"></div>

    <h2 class="heading" style="top:262px">channel catfish</h2>
    <div class="table" style="top:303px;left:83px;grid-template-columns:109px 85px auto">
      <span class="th">Size</span><span class="th">Each</span><span class="th">1000</span>
      <span>6-8 Inch</span><span>65¢</span><span>60¢</span>
    </div>
    <div class="rule" style="top:360px"></div>

    <h2 class="heading" style="top:376px">albino catfish</h2>
    <p class="sub" style="top:405px">(March &amp; April)</p>
    <div class="table" style="top:445px;left:113px;grid-template-columns:135px auto">
      <span class="th">Size</span><span class="th">Each</span>
      <span>5-8 Inch</span><span>$1.20</span>
    </div>
    <div class="rule" style="top:504px"></div>

    <h2 class="heading" style="top:521px">black crappie</h2>
    <p class="sub" style="top:549px">(March &amp; April)</p>
    <div class="table" style="top:588px;left:113px;grid-template-columns:135px auto">
      <span class="th">Size</span><span class="th">Each</span>
      <span>3-5 Inch</span><span>$1.10</span>
    </div>
    <div class="rule" style="top:644px"></div>

    <h2 class="heading" style="top:656px">fathead minnows</h2>
    <p class="lines" style="top:697px">$36.00 per thousand<br>($9.00 per lb.)</p>

    <svg class="photo photo--bottom" viewBox="0 700 400 315" role="img" aria-label="Photo of a net scooping fish from a holding tank">
      <defs><linearGradient id="gm" x1="0" y1="0" x2="1" y2="1"><stop offset="0" stop-color="#7f8a86"/><stop offset=".5" stop-color="#b8b9a8"/><stop offset="1" stop-color="#4d4a3a"/></linearGradient></defs>
      <path d="M0 904Q200 712 400 904V1015H0Z" fill="url(#gm)"/>
      <path d="M0 904Q200 712 400 904" fill="none" stroke="#2b3a9e" stroke-width="9"/>
      <path d="M0 894Q200 702 400 894" fill="none" stroke="#6f8fe0" stroke-width="2" stroke-dasharray="6 5"/>
    </svg>
  </section>

  <!-- Right panel -->
  <section class="panel panel--right">
    <svg class="photo photo--top" viewBox="0 0 400 250" role="img" aria-label="Photo of a family seining fish at the edge of a pond">
      <defs><linearGradient id="gr" x1="0" y1="0" x2="1" y2="1"><stop offset="0" stop-color="#8f9a84"/><stop offset=".5" stop-color="#a9a58c"/><stop offset="1" stop-color="#5c6e52"/></linearGradient></defs>
      <path d="M0 0H400V150Q200 314 0 150Z" fill="url(#gr)"/>
      <path d="M0 150Q200 314 400 150" fill="none" stroke="#2b3a9e" stroke-width="9"/>
      <path d="M0 160Q200 324 400 160" fill="none" stroke="#4a5fc0" stroke-width="2" stroke-dasharray="6 5"/>
    </svg>

    <h2 class="heading" style="top:275px">golden shiners</h2>
    <p class="sub sub--blue" style="top:306px">(Delivery Only – Minimum 50 lb.)</p>
    <div class="table" style="top:339px;left:120px;grid-template-columns:98px auto">
      <span>50-99 lb.</span><span>$8.00 lb.</span>
      <span>100+ lb.</span><span>$7.50 lb.</span>
    </div>
    <div class="rule" style="top:386px"></div>

    <h2 class="heading" style="top:397px">floating fish food</h2>
    <p class="lines" style="top:433px">Starter Size (50 lb. Bag)<br>41% Protein<br>Market Price – Inquire<br>(Only Available at Farm)</p>
    <div class="rule" style="top:531px"></div>

    <h2 class="heading" style="top:542px">tilapia</h2>
    <p class="sub" style="top:572px">(May 15 – June 30)</p>
    <p class="lines" style="top:607px">5-10 Tilapia per lb.</p>
    <div class="table" style="top:627px;left:114px;grid-template-columns:92px auto">
      <span>1-25 lb.</span><span>$15.00 lb.</span>
      <span>26-40 lb.</span><span>$14.00 lb.</span>
      <span>40-50 lb.</span><span>$13.00 lb.</span>
      <span>50+ lb.</span><span>$12.00 lb.</span>
    </div>
    <div class="rule" style="top:722px"></div>

    <h2 class="heading" style="top:729px">japanese koi</h2>
    <div class="table" style="top:769px;left:112px;grid-template-columns:136px auto">
      <span class="th">Size</span><span class="th">Each</span>
      <span>4-5 Inch</span><span>$6.00</span>
      <span>6-8 Inch</span><span>$10.00</span>
      <span>*9-12 Inch</span><span>$15.00</span>
    </div>
    <div class="rule" style="top:861px"></div>

    <p class="note note--blue" style="top:868px;line-height:28px">BUTTERFLY KOI<br>ALSO AVAILABLE!</p>
    <div class="dots" style="top:930px"></div>
    <p class="note" style="top:937px">PRICES SUBJECT TO CHANGE<br>WITHOUT NOTICE</p>
  </section>

</div>
</body>
</html>
```